Paws Of Kindness Business cards

Design a cool, modern business card for my bully breed rescue.

Contact Information for Business Card

Marlene
517-382-4061 Marlene@PawsOfKindnessRescue.net PawsOfKindnessRescue.net

Font styles to use
Serif
Sans Serif

Colors

Designer to choose colors to be used in the design.

Requirements
Must have
• logo and info. Color
Nice to have
• Foil. Maybe some paw prints on the back or some kind of dog illustration.

```html
<!DOCTYPE html>
<html lang="en">
<head>
<meta charset="utf-8">
<title>Paws Of Kindness – Business Card</title>
<link rel="stylesheet" href="https://fonts.googleapis.com/css2?family=Noto+Serif:wght@400&family=Open+Sans:wght@400&display=swap">
<style>
  :root {
    --page-bg: #3a3f46;
    --card-white: #ffffff;
    --card-black: #0b0b0b;
    --ink: #111111;
    --text-light: #ffffff;
    --rule: #f2f2f2;
  }
  * { box-sizing: border-box; margin: 0; padding: 0; }
  html, body {
    width: 1200px; height: 960px; overflow: hidden;
    background: var(--page-bg);
  }
  .stage {
    width: 1200px; height: 960px;
    display: flex; align-items: center; justify-content: center;
  }
  .card {
    position: relative;
    width: 1050px; height: 600px;
    background: var(--card-white);
    overflow: hidden;
  }
  .brand {
    position: absolute; top: 0; left: 0; right: 0; height: 250px;
    display: flex; align-items: center; justify-content: center; gap: 22px;
  }
  .brand-circle {
    width: 56px; height: 56px; border-radius: 50%;
    border: 3px solid var(--ink);
  }
  .brand-name {
    font-family: "Noto Serif", serif;
    font-weight: 400; font-size: 54px; color: var(--ink);
    letter-spacing: 1px;
  }
  .info-band {
    position: absolute; left: 0; right: 0; top: 250px; bottom: 20px;
    background: var(--card-black);
    display: flex; align-items: center;
  }
  .holder {
    width: 430px; text-align: right; padding-right: 48px;
    font-family: "Noto Serif", serif;
    font-size: 50px; color: var(--text-light);
  }
  .divider {
    width: 2px; height: 170px; background: var(--text-light);
  }
  .contacts {
    list-style: none; padding-left: 36px;
    font-family: "Open Sans", sans-serif;
    font-size: 27px; color: var(--text-light);
  }
  .contacts li {
    display: flex; align-items: center; gap: 18px; line-height: 1.6;
  }
  .contacts svg { width: 28px; height: 28px; flex: none; }
  .card-edge {
    position: absolute; left: 0; right: 0; bottom: 0; height: 20px;
    background: var(--card-white);
    border-top: 4px solid var(--rule);
  }
</style>
</head>
<body>
<main class="stage">
  <article class="card">
    <header class="brand">
      <span class="brand-circle" aria-hidden="true"></span>
      <span class="brand-name">Paws Of Kindness</span>
    </header>
    <section class="info-band">
      <h1 class="holder">Marlene</h1>
      <span class="divider" aria-hidden="true"></span>
      <ul class="contacts">
        <li>
          <svg viewBox="0 0 24 24" aria-hidden="true"><rect x="1" y="1" width="22" height="22" rx="4" fill="#fff"/><path d="M8 5l2.5 3-1.5 1.8c.9 2 2.4 3.5 4.3 4.3L15 12.6l3 2.4-1.3 2.7c-5.4-.5-9.3-4.5-9.8-9.8z" fill="#0b0b0b"/></svg>
          <span>517-382-4061</span>
        </li>
        <li>
          <svg viewBox="0 0 24 24" aria-hidden="true"><rect x="2" y="5" width="20" height="14" fill="none" stroke="#fff" stroke-width="2"/><path d="M2 6l10 7 10-7" fill="none" stroke="#fff" stroke-width="2"/></svg>
          <span>Marlene@PawsOfKindnessRescue.net</span>
        </li>
        <li>
          <svg viewBox="0 0 24 24" aria-hidden="true"><rect x="1" y="1" width="22" height="22" rx="4" fill="#fff"/><circle cx="12" cy="12" r="7" fill="none" stroke="#0b0b0b" stroke-width="1.8"/><path d="M5 12h14M12 5c-3 3.5-3 10.5 0 14M12 5c3 3.5 3 10.5 0 14" fill="none" stroke="#0b0b0b" stroke-width="1.5"/></svg>
          <span>PawsOfKindnessRescue.net</span>
        </li>
      </ul>
    </section>
    <div class="card-edge" aria-hidden="true"></div>
  </article>
</main>
</body>
</html>
```